Website Design for new Custom Homebuilder company R Calloway Homes

We need a website design for a new company based out of Liberty Hill, Texas called R Calloway Homes. We specialize in building unique, high end custom homes in Liberty Hill, Texas and the surrounding area. We would like to see designs that use the color black, white, copper and gold. Website needs to have a modern feel and the pages that have information about the company and then pages that have a gallery with pictures of completed homes and a page that has information on available homes.

```html
<!DOCTYPE html>
<html lang="en">
<head>
<meta charset="utf-8">
<title>R Calloway Homes</title>
<link href="https://fonts.googleapis.com/css2?family=Roboto:ital,wght@0,400;0,500;0,700;1,400&family=Montserrat:wght@500;600;700&display=swap" rel="stylesheet">
<style>
:root{
  --black:#050505;
  --charcoal:#252423;
  --charcoal-2:#1a1918;
  --copper:#a86d3f;
  --copper-dark:#8a5a33;
  --gold:#c38a55;
  --white:#ffffff;
  --muted:#8c8a88;
  --field:#3a3938;
}
*{margin:0;padding:0;box-sizing:border-box}
html,body{width:1200px;height:4850px;overflow:hidden;background:var(--black)}
body{position:relative;font-family:"Roboto",sans-serif;color:var(--white)}
.abs{position:absolute}
.nav-link{position:absolute;top:108px;font-family:"Montserrat",sans-serif;font-weight:600;font-size:13px;letter-spacing:.5px;color:var(--white)}
.photo{position:absolute}
.hero-title{position:absolute;top:256px;left:0;width:1200px;text-align:center;font-weight:700;font-size:56px;line-height:64px;letter-spacing:1px;text-transform:uppercase}
.btn{position:absolute;display:flex;align-items:center;justify-content:center;gap:14px;font-family:"Montserrat",sans-serif;font-weight:700;font-size:15px;letter-spacing:.5px;border-radius:30px;color:var(--white)}
.section-title{position:absolute;font-size:42px;font-weight:500}
.section-title span{color:var(--gold)}
.body-copy{position:absolute;font-size:13px;line-height:15px;color:var(--white)}
.read-more{position:absolute;display:flex;align-items:center;gap:16px;font-family:"Montserrat",sans-serif;font-weight:700;font-size:15px;letter-spacing:.4px}
.card-title{position:absolute;font-family:"Montserrat",sans-serif;font-weight:700;font-size:15px;color:var(--copper);letter-spacing:.3px}
.card-copy{position:absolute;font-size:12.5px;line-height:16px;color:#4d4b49;width:310px}
.arrow-box{position:absolute;width:49px;height:48px;background:var(--white);display:flex;align-items:center;justify-content:center}
.testimonial{position:absolute;width:410px;height:308px;border:2px solid var(--copper);background:var(--charcoal)}
.testimonial-shadow{position:absolute;width:410px;height:308px;border:2px solid var(--copper)}
.testimonial .quote{position:absolute;left:54px;top:32px;font-family:"Roboto",serif;font-style:italic;font-weight:700;font-size:90px;line-height:80px;color:var(--copper)}
.testimonial p{position:absolute;left:53px;top:114px;width:320px;font-style:italic;font-size:16px;line-height:19px;color:var(--copper)}
.testimonial .client{position:absolute;left:57px;top:258px;font-family:"Montserrat",sans-serif;font-size:15px;letter-spacing:4px;color:var(--muted);text-transform:uppercase}
.contact-item{position:absolute;left:213px}
.contact-item h4{font-family:"Montserrat",sans-serif;font-weight:700;font-size:13px;letter-spacing:.3px;margin-left:34px}
.contact-item p{font-size:11px;line-height:14px;margin-left:34px;margin-top:3px}
.contact-item svg{position:absolute;left:0;top:0}
.field{position:absolute;height:36px;background:var(--field);font-family:"Montserrat",sans-serif;font-weight:600;font-size:10.5px;color:var(--white);padding:13px 0 0 18px}
.field svg{position:absolute;right:14px;top:14px}
</style>
</head>
<body>

<!-- Hero -->
<div class="photo" role="img" aria-label="Aerial view of a suburban neighbourhood at sunset" style="left:0;top:0;width:1200px;height:860px;background:linear-gradient(180deg,#1c1d22 0%,#3a2a22 22%,#5a3a26 30%,#2c2a2a 45%,#2e3136 70%,#1b1c1e 100%)"></div>

<header>
  <div class="abs" style="left:125px;top:41px;display:flex;align-items:center;gap:10px;font-family:'Montserrat',sans-serif;font-weight:600;font-size:16px;color:var(--copper)">
    <svg width="18" height="18" viewBox="0 0 24 24"><path fill="#a86d3f" d="M6.6 10.8a15.1 15.1 0 0 0 6.6 6.6l2.2-2.2c.3-.3.7-.4 1-.2 1.1.4 2.3.6 3.6.6.6 0 1 .4 1 1V20c0 .6-.4 1-1 1A17 17 0 0 1 3 4c0-.6.4-1 1-1h3.5c.6 0 1 .4 1 1 0 1.3.2 2.5.6 3.6.1.3 0 .7-.2 1z"/></svg>
    512 555 0148
  </div>
  <div class="nav-link" style="left:124px">HOME</div>
  <div class="nav-link" style="left:215px">ABOUT US</div>
  <div class="nav-link" style="left:337px">SERVICES</div>
  <div class="abs" style="left:440px;top:96px;width:320px;text-align:center;font-family:'Montserrat',sans-serif;font-weight:500;font-size:26px;letter-spacing:14px;color:var(--white)">R CALLOWAY</div>
  <div class="abs" style="left:440px;top:131px;width:320px;text-align:center;font-family:'Montserrat',sans-serif;font-weight:500;font-size:11px;letter-spacing:6px;color:var(--copper)">HOMES</div>
  <div class="nav-link" style="left:826px">HOMES</div>
  <div class="nav-link" style="left:927px">GALLERY</div>
  <div class="nav-link" style="left:1042px">CONTACT</div>
  <div class="abs" style="left:848px;top:48px;display:flex;gap:10px">
    <span style="width:16px;height:16px;background:var(--white);border-radius:2px"></span>
    <span style="width:16px;height:16px;background:var(--white);border-radius:2px"></span>
    <span style="width:16px;height:16px;background:var(--white);border-radius:2px"></span>
    <span style="width:16px;height:16px;background:var(--white);border-radius:2px"></span>
  </div>
  <div class="btn" style="left:974px;top:36px;width:147px;height:38px;background:var(--copper);font-size:12px">GET A QUOTE</div>
  <div class="abs" style="left:0;top:169px;width:1200px;height:1px;background:rgba(255,255,255,.35)"></div>
</header>

<h1 class="hero-title">Welcome to<br>R Calloway Homes</h1>
<div class="btn" style="left:495px;top:399px;width:208px;height:62px;background:var(--black)">GET STARTED
  <svg width="20" height="12" viewBox="0 0 20 12"><path d="M0 6h18M13 1l5 5-5 5" stroke="#fff" stroke-width="1.8" fill="none"/></svg></div>
<svg class="abs" style="left:580px;top:631px" width="40" height="12">
  <circle cx="6" cy="6" r="4" fill="none" stroke="#fff" stroke-width="1.3"/>
  <circle cx="20" cy="6" r="4.5" fill="#fff"/>
  <circle cx="34" cy="6" r="4" fill="none" stroke="#fff" stroke-width="1.3"/>
</svg>

<svg class="abs" style="left:0;top:740px" width="1200" height="125">
  <polygon points="0,117 603,6 1200,117 1200,125 0,125" fill="#050505"/>
  <polyline points="0,117 603,6 1200,117" fill="none" stroke="#a86d3f" stroke-width="5"/>
</svg>

<!-- About -->
<section>
  <svg class="abs" style="left:188px;top:918px" width="370" height="360" viewBox="0 0 370 360">
    <polygon points="185,2 366,92 366,268 185,358 4,268 4,92" fill="none" stroke="#a86d3f" stroke-width="3"/>
  </svg>
  <div class="photo" role="img" aria-label="Builder in a hard hat and safety harness at work" style="left:200px;top:930px;width:346px;height:336px;clip-path:polygon(50% 0,100% 25%,100% 75%,50% 100%,0 75%,0 25%);background:linear-gradient(135deg,#6b5a44,#3b3128 55%,#8a7356)"></div>
  <h2 class="section-title" style="left:675px;top:985px">About <span>R Calloway</span></h2>
  <p class="body-copy" style="left:675px;top:1054px;width:380px">Lorem ipsum dolor sit amet, consectetur adipiscing elit, sed do eiusmod tempor incididunt ut labore et dolore magna aliqua. Quis ipsum suspendisse ultrices gravida. Risus commod</p>
  <div class="read-more" style="left:682px;top:1142px;color:var(--copper)">READ MORE
    <svg width="20" height="12"><path d="M0 6h18M13 1l5 5-5 5" stroke="#a86d3f" stroke-width="1.8" fill="none"/></svg></div>
</section>

<!-- Services split -->
<section>
  <div class="photo" role="img" aria-label="Large modern building tinted in copper" style="left:0;top:1320px;width:603px;height:480px;clip-path:polygon(0 0,100% 17%,100% 85%,0 100%);background:linear-gradient(180deg,#9a6a42,#7a4f2e 55%,#8e5e37)"></div>
  <div class="photo" role="img" aria-label="Custom home exterior in dim light" style="left:603px;top:1330px;width:597px;height:470px;clip-path:polygon(0 16%,100% 0,100% 100%,0 86%);background:linear-gradient(180deg,#2d2c2b,#3b3a39 60%,#242322)"></div>
  <svg class="abs" style="left:106px;top:1518px" width="70" height="76" viewBox="0 0 70 76">
    <g fill="none" stroke="#fff" stroke-width="3">
      <path d="M4 74h62M10 74V20l30-16v70M40 30h22v44"/>
      <path d="M16 28h18M16 38h18M16 48h18M16 58h18M46 40h10M46 50h10M46 60h10"/>
    </g>
  </svg>
  <h3 class="abs" style="left:200px;top:1508px;font-size:36px;font-weight:400">Unique Buildings</h3>
  <p class="body-copy" style="left:200px;top:1568px;width:320px;font-size:12.5px">Lorem ipsum dolor sit amet, consectetur adipiscing elit, sed do eiusmod tempor incididunt ut labore et dolore magna aliqua. Quis ipsum suspendisse ultrices gravida. Risus commod</p>
  <div class="read-more" style="left:213px;top:1662px">READ MORE
    <svg width="20" height="12"><path d="M0 6h18M13 1l5 5-5 5" stroke="#fff" stroke-width="1.8" fill="none"/></svg></div>

  <svg class="abs" style="left:1036px;top:1512px" width="96" height="100" viewBox="0 0 96 100">
    <g fill="none" stroke="#fff" stroke-width="4" stroke-linejoin="round">
      <path d="M4 48L48 6l44 42M16 38v58h64V38"/><path d="M38 96V66h20v30"/>
    </g>
  </svg>
  <h3 class="abs" style="left:700px;top:1508px;width:312px;text-align:right;font-size:36px;font-weight:400">Custom Homes</h3>
  <p class="body-copy" style="left:692px;top:1568px;width:320px;text-align:right;font-size:12.5px">Lorem ipsum dolor sit amet, consectetur adipiscing elit, sed do eiusmod tempor incididunt ut labore et dolore magna aliqua. Quis ipsum suspendisse ultrices gravida. Risus commod</p>
  <div class="read-more" style="left:856px;top:1662px;color:var(--copper)">READ MORE
    <svg width="20" height="12"><path d="M0 6h18M13 1l5 5-5 5" stroke="#a86d3f" stroke-width="1.8" fill="none"/></svg></div>
</section>

<!-- Available homes -->
<section>
  <div class="photo" role="img" aria-label="Faint house silhouette in the background" style="left:0;top:2170px;width:1200px;height:340px;background:linear-gradient(180deg,#050505,#141312 60%,#1c1b1a)"></div>
  <h2 class="section-title" style="left:158px;top:1864px">Available <span>Homes</span></h2>
  <p class="body-copy" style="left:156px;top:1950px;width:380px;font-size:12.5px">Lorem ipsum dolor sit amet, consectetur adipiscing elit, sed do eiusmod tempor incididunt ut labore et dolore magna aliqua. Quis ipsum suspendisse ultrices gravida. Risus commod</p>

  <div class="photo" role="img" aria-label="Bright living room with fireplace" style="left:170px;top:2035px;width:320px;height:223px;background:linear-gradient(160deg,#d9d6d0,#9c9a95 50%,#4d4a47)"></div>
  <div class="arrow-box" style="left:422px;top:2234px"><svg width="18" height="12"><path d="M0 6h16M11 1l5 5-5 5" stroke="#222" stroke-width="1.6" fill="none"/></svg></div>
  <div class="card-title" style="left:170px;top:2300px">CONTRARY TO POPULAR</div>
  <p class="card-copy" style="left:170px;top:2330px">Lorem ipsum dolor sit amet, consectetur adipiscing elit, sed do eiusmod tempor</p>

  <div class="photo" role="img" aria-label="White two-storey house at dusk" style="left:533px;top:2035px;width:320px;height:223px;background:linear-gradient(160deg,#2a4c8a,#6a7ea8 45%,#c9c2b4 70%,#5a5a5a)"></div>
  <div class="arrow-box" style="left:785px;top:2234px"><svg width="18" height="12"><path d="M0 6h16M11 1l5 5-5 5" stroke="#222" stroke-width="1.6" fill="none"/></svg></div>
  <div class="card-title" style="left:533px;top:2300px">CONTRARY TO POPULAR</div>
  <p class="card-copy" style="left:533px;top:2330px">Lorem ipsum dolor sit amet, consectetur adipiscing elit, sed do eiusmod tempor</p>

  <div class="photo" role="img" aria-label="Modern apartment building with terraces" style="left:889px;top:2035px;width:311px;height:223px;background:linear-gradient(170deg,#b9c6d4,#dfe2e2 45%,#8a9a80)"></div>
  <div class="arrow-box" style="left:1141px;top:2234px"><svg width="18" height="12"><path d="M0 6h16M11 1l5 5-5 5" stroke="#222" stroke-width="1.6" fill="none"/></svg></div>
  <div class="card-title" style="left:889px;top:2300px">CONTRARY TO POPULAR</div>
  <p class="card-copy" style="left:889px;top:2330px">Lorem ipsum dolor sit amet, consectetur adipiscing elit, sed do eiusmod tempor</p>
</section>

<!-- Testimonials -->
<section>
  <div class="abs" style="left:0;top:2500px;width:1200px;height:705px;background:var(--charcoal)"></div>
  <svg class="abs" style="left:0;top:2498px" width="1200" height="106"><polygon points="0,0 1200,0 1200,4 603,104 0,4" fill="#171615"/></svg>
  <h2 class="section-title" style="left:0;top:2670px;width:1200px;text-align:center;color:var(--white)">Client <span>Testimonials</span></h2>

  <div class="testimonial-shadow" style="left:164px;top:2807px"></div>
  <div class="testimonial" style="left:151px;top:2794px">
    <div class="quote">&ldquo;</div>
    <p>Lorem ipsum dolor sit amet, consectetur adipiscing elit, sed do eiusmod tempor incididunt ut labore et dolore magna aliqua. Quis ipsum suspendisse ultrices gravida. Risus commodo viverra maecenas accumsan lacus vel facilisis.</p>
    <div class="client">Dana Whitfield</div>
  </div>

  <div class="testimonial-shadow" style="left:631px;top:2807px"></div>
  <div class="testimonial" style="left:618px;top:2794px">
    <div class="quote">&ldquo;</div>
    <p>Lorem ipsum dolor sit amet, consectetur adipiscing elit, sed do eiusmod tempor incididunt ut labore et dolore magna aliqua. Quis ipsum suspendisse ultrices gravida. Risus commodo viverra maecenas accumsan lacus vel facilisis.</p>
    <div class="client">Dana Whitfield</div>
  </div>
</section>

<!-- Gallery -->
<section>
  <h2 class="section-title" style="left:0;top:3337px;width:1200px;text-align:center">Completed <span>Homes (Gallery)</span></h2>
  <div class="photo" role="img" aria-label="Navy craftsman house with stone path" style="left:149px;top:3431px;width:333px;height:476px;background:linear-gradient(180deg,#9fb4c8,#3c4660 40%,#4a5636 75%,#3f6b2a)"></div>
  <div class="photo" role="img" aria-label="Modern house with garage at dusk" style="left:507px;top:3431px;width:247px;height:231px;background:linear-gradient(180deg,#7f93b0,#48505a 50%,#7a4f36)"></div>
  <div class="photo" role="img" aria-label="Stone and timber house on a lawn" style="left:786px;top:3431px;width:264px;height:350px;background:linear-gradient(180deg,#8da3b8,#5d5148 50%,#5f7a33)"></div>
  <div class="photo" role="img" aria-label="Timber-framed house under blue sky" style="left:507px;top:3689px;width:247px;height:216px;background:linear-gradient(180deg,#1f4f9a,#7a6a3c 55%,#a2743c)"></div>
  <div class="photo" role="img" aria-label="White farmhouse in a field at sunset" style="left:151px;top:3930px;width:603px;height:209px;background:linear-gradient(180deg,#5d5a58,#8a7a6a 45%,#4a4e34)"></div>
  <div class="photo" role="img" aria-label="Grey-blue house with gables and clouds" style="left:786px;top:3809px;width:264px;height:330px;background:linear-gradient(180deg,#6f96c8,#c2cbd4 35%,#5a6670 65%,#4b6a32)"></div>
  <div class="btn" style="left:507px;top:4183px;width:186px;height:52px;background:var(--copper)">VIEW MORE
    <svg width="20" height="12"><path d="M0 6h18M13 1l5 5-5 5" stroke="#fff" stroke-width="1.8" fill="none"/></svg></div>
</section>

<!-- Contact -->
<section>
  <div class="abs" style="left:0;top:4296px;width:1200px;height:554px;background:var(--charcoal-2)"></div>
  <svg class="abs" style="left:0;top:4290px" width="1200" height="76">
    <polygon points="0,0 1200,0 1200,6 603,71 0,6" fill="#050505"/>
    <polyline points="0,6 603,71 1200,6" fill="none" stroke="#a86d3f" stroke-width="2"/>
  </svg>

  <h2 class="abs" style="left:213px;top:4455px;font-family:'Montserrat',sans-serif;font-weight:700;font-size:30px">CONTACT US</h2>
  <div class="contact-item" style="top:4520px">
    <svg width="20" height="26" viewBox="0 0 20 26"><path d="M10 1a8 8 0 0 0-8 8c0 6 8 16 8 16s8-10 8-16a8 8 0 0 0-8-8z" fill="none" stroke="#a86d3f" stroke-width="2"/><circle cx="10" cy="9" r="3" fill="#a86d3f"/></svg>
    <h4>ADDRESS</h4><p>318 Cedar Run Trail<br>Pinecrest, Oregon 97031</p>
  </div>
  <div class="contact-item" style="top:4592px">
    <svg width="20" height="20" viewBox="0 0 24 24"><path fill="#a86d3f" d="M6.6 10.8a15.1 15.1 0 0 0 6.6 6.6l2.2-2.2c.3-.3.7-.4 1-.2 1.1.4 2.3.6 3.6.6.6 0 1 .4 1 1V20c0 .6-.4 1-1 1A17 17 0 0 1 3 4c0-.6.4-1 1-1h3.5c.6 0 1 .4 1 1 0 1.3.2 2.5.6 3.6.1.3 0 .7-.2 1z"/></svg>
    <h4>CALL NOW</h4><p>512 555 0148</p>
  </div>
  <div class="contact-item" style="top:4648px">
    <svg width="20" height="16" viewBox="0 0 20 16"><rect x="1" y="2" width="18" height="12" fill="none" stroke="#a86d3f" stroke-width="2"/><path d="M1 2l9 7 9-7" fill="none" stroke="#a86d3f" stroke-width="2"/></svg>
    <h4>EMAIL NOW</h4><p>hello@rcallowayhomes.com</p>
  </div>
  <div class="contact-item" style="top:4705px">
    <svg width="20" height="20" viewBox="0 0 20 20"><g fill="none" stroke="#a86d3f" stroke-width="1.6"><circle cx="10" cy="10" r="8.5"/><ellipse cx="10" cy="10" rx="4" ry="8.5"/><path d="M1.5 10h17M3 5.5h14M3 14.5h14"/></g></svg>
    <h4>WEBSITE</h4><p>www.rcallowayhomes.com</p>
  </div>

  <h3 class="abs" style="left:539px;top:4461px;font-family:'Montserrat',sans-serif;font-weight:700;font-size:17px">GET A QUOTE</h3>
  <div class="field" style="left:539px;top:4505px;width:232px">First Name</div>
  <div class="field" style="left:793px;top:4505px;width:230px">Last Name</div>
  <div class="field" style="left:539px;top:4555px;width:232px">Phone Number</div>
  <div class="field" style="left:793px;top:4555px;width:230px">Email Address</div>
  <div class="field" style="left:539px;top:4604px;width:232px">Select Your Service
    <svg width="10" height="6"><path d="M1 1l4 4 4-4" stroke="#fff" fill="none" stroke-width="1.3"/></svg></div>
  <div class="field" style="left:793px;top:4604px;width:230px">Select City
    <svg width="10" height="6"><path d="M1 1l4 4 4-4" stroke="#fff" fill="none" stroke-width="1.3"/></svg></div>
  <div class="field" style="left:539px;top:4654px;width:484px;height:88px">Message Here......</div>
  <div class="abs" style="left:859px;top:4695px;width:158px;height:41px;background:var(--copper);border-radius:3px;display:flex;align-items:center;justify-content:center;gap:28px;font-family:'Montserrat',sans-serif;font-weight:700;font-size:15px">SUBMIT
    <svg width="20" height="12"><path d="M0 6h18M13 1l5 5-5 5" stroke="#fff" stroke-width="1.8" fill="none"/></svg></div>

  <p class="abs" style="left:0;top:4792px;width:1200px;text-align:center;font-size:11px">© 2022 R Calloway Homes . All Rights Reserved.</p>
</section>

</body>
</html>
```